Business card for our large format printing and installation business

We want a professional looking business card for our business. We manufacture and install Signs.

On the back of the card add this info
Large Format Graphics Printing & Installations, Event Graphics, Banners, Posters, Vehicle Fleet Graphics, Boat Wraps, Wall Murals, Decals,Displays,Signs,Plaques,Digital Signs

On the Front of the card add the Tallowfern Signs logo, plus On the back of the card add the Orange Tallowfern Wraps logo. The 2 vector logos are attached to the design brief.

Target Market(s)

Local business owners

Contact Information for Business Card

Colors
f37122
f68d4e
f9ba93

Requirements
Must have
• On the Front of the card add the Tallowfern Signs logo, plus On the back of the card add the Orange Tallowfern Wraps logo. The 2 vector logos are attached to the design brief.

```html
<!DOCTYPE html>
<html lang="en">
<head>
<meta charset="utf-8">
<title>Tallowfern Business Card</title>
<link href="https://fonts.googleapis.com/css2?family=Roboto:wght@400;500;700;900&display=swap" rel="stylesheet">
<style>
  :root {
    --bg: #a3a3a3;
    --card-dark: #2a2a2a;
    --card-light: #ffffff;
    --brand-orange: #f39a1e;
    --brand-yellow: #f8c31c;
    --text-light: #f2f2f2;
    --text-gray: #5a5a5a;
  }
  * { margin: 0; padding: 0; box-sizing: border-box; }
  html, body { width: 1133px; height: 1200px; overflow: hidden; }
  body {
    background: var(--bg);
    font-family: "Roboto", Arial, sans-serif;
    position: relative;
  }
  .card {
    position: absolute;
    left: 219px;
    width: 694px;
    height: 397px;
  }
  .card--back { top: 153px; background: var(--card-dark); }
  .card--front { top: 649px; background: var(--card-light); }

  .brand-name {
    position: absolute;
    font-weight: 900;
    color: var(--brand-orange);
    line-height: 1;
    white-space: nowrap;
  }
  .card--back .brand-name {
    left: 0; right: 0;
    top: 140px;
    text-align: center;
    font-size: 58px;
    letter-spacing: -0.5px;
  }
  .card--front .brand-name {
    right: 34px;
    top: 58px;
    font-size: 36px;
    letter-spacing: -0.3px;
  }

  .services {
    position: absolute;
    left: 0; right: 0;
    top: 325px;
    text-align: center;
    color: var(--text-light);
    font-size: 16px;
    line-height: 22px;
  }
  .services .dot {
    display: inline-block;
    width: 5px; height: 5px;
    border-radius: 50%;
    background: var(--brand-yellow);
    vertical-align: middle;
    margin: 0 5px 2px;
  }

  .contact {
    position: absolute;
    left: 31px;
    top: 156px;
    color: var(--text-gray);
  }
  .contact__name {
    color: var(--brand-orange);
    font-weight: 700;
    font-size: 25px;
    line-height: 30px;
    margin-bottom: 10px;
  }
  .contact__address {
    font-size: 18.5px;
    line-height: 26px;
    margin-bottom: 12px;
  }
  .contact__list { list-style: none; font-size: 18.5px; }
  .contact__list li {
    display: flex;
    align-items: center;
    height: 25.5px;
  }
  .contact__list svg {
    width: 15px; height: 15px;
    margin-right: 7px;
    flex-shrink: 0;
  }
</style>
</head>
<body>

  <section class="card card--back" aria-label="Card back">
    <div class="brand-name">Tallowfern Wraps</div>
    <p class="services">
      Large Format Graphics Printing &amp; Installations<span class="dot"></span>Banners<span class="dot"></span>Posters<span class="dot"></span>Vehicle Graphics<br>
      Boat Wraps<span class="dot"></span>Wall Murals<span class="dot"></span>Decals<span class="dot"></span>Displays<span class="dot"></span>Signs<span class="dot"></span>Plaques<span class="dot"></span>Digital Signs
    </p>
  </section>

  <section class="card card--front" aria-label="Card front">
    <div class="brand-name">Tallowfern Signs</div>
    <div class="contact">
      <h1 class="contact__name">Marco Ellison</h1>
      <p class="contact__address">1840 Harbor Crest Lane #7<br>Seaview Point, FL 33120</p>
      <ul class="contact__list">
        <li>
          <svg viewBox="0 0 16 16" aria-hidden="true"><path fill="#f39a1e" d="M3.5 1.5l2.3 2.6-1.2 2c.9 1.9 2.3 3.4 4.3 4.4l2-1.2 2.6 2.3-1.4 2.4C7 14 2 9 1.1 2.9z"/></svg>
          555-204-7781
        </li>
        <li>
          <svg viewBox="0 0 16 16" aria-hidden="true"><rect x="4" y="1" width="8" height="14" rx="1.5" fill="none" stroke="#f39a1e" stroke-width="1.6"/><circle cx="8" cy="12.5" r="0.9" fill="#f39a1e"/></svg>
          555-318-4426
        </li>
        <li>
          <svg viewBox="0 0 16 16" aria-hidden="true"><rect x="1.5" y="4" width="13" height="9" fill="#f39a1e"/><path d="M1.5 4L8 9l6.5-5" fill="none" stroke="#fff" stroke-width="1.2"/></svg>
          marco@tallowfern.net
        </li>
        <li>
          <svg viewBox="0 0 16 16" aria-hidden="true"><circle cx="8" cy="8" r="6.5" fill="none" stroke="#f39a1e" stroke-width="1.6"/><ellipse cx="8" cy="8" rx="2.6" ry="6.5" fill="none" stroke="#f39a1e" stroke-width="1.2"/><path d="M1.5 8h13" stroke="#f39a1e" stroke-width="1.2"/></svg>
          www.tallowfernwraps.com
        </li>
      </ul>
    </div>
  </section>

</body>
</html>
```